PowerPoint Template Needed for Investment Firm

Norvelle Capital Management is an emerging wealth management firm based in New Jersey. It offers superior investment returns to high net worth individuals and institutions by finding undervalued assets.

We recently selected a company logo which was inspired by the Tucana constellation. Beta Tucanae is a group of six stars, containing star cluster 47 Tucanae, rated the second brightest object in the sky.

Now we need a PowerPoint template with the designs for the following:

1. Title/cover page slide
2. Content slide with title
3. Section slide - to introduce a new section
4. Final slide - with contact information

The slides will be used at investor presentations, that is, to provide information about the company to potential investors. Since we are an investment firm, the design should project a sense of stability, growth and professionalism. The owner is interested in something simple yet striking, which of course is consistent with the logo. I'm thinking more conservative colors and Sans Serif fonts.

I plan on changing the status to non-refundable once I see some designs that I really like.

Target Market(s)

Wealthy individuals, probably middle aged or older, in the US

Industry/Entity Type

Conservative

Requirements
Must have
• Sans serif fonts
Clean, very professional look
Conservative colors that complement existing logo
Should not have
• Anything too busy or complicated

```html
<!DOCTYPE html>
<html lang="en">
<head>
<meta charset="utf-8">
<title>Norvelle Capital Management – Slide Template</title>
<link href="https://fonts.googleapis.com/css2?family=PT+Sans:wght@400;700&family=Arimo:wght@400;700&display=swap" rel="stylesheet">
<style>
  :root{
    --stage:#e9e6e1;
    --navy:#1b2a8c;
    --navy-deep:#0d1760;
    --royal:#2c46a6;
    --title-blue:#1f3f9e;
    --footer:#2946a0;
    --lavender:#a79ad6;
    --lavender-light:#d6cff0;
    --text:#4a4a4a;
    --bullet:#2a3f8f;
    --white:#ffffff;
  }
  *{box-sizing:border-box;margin:0;padding:0}
  html,body{width:1200px;height:465px;overflow:hidden;background:var(--stage)}
  .deck{position:relative;width:1200px;height:465px}
  .slide{position:absolute;width:265px;height:199px;overflow:hidden;background:linear-gradient(160deg,#ffffff 0%,#f3f4f8 60%,#e9ebf2 100%);font-family:"PT Sans",sans-serif;color:var(--text);box-shadow:0 1px 3px rgba(0,0,0,.25)}
  .r1{top:7px}.r2{top:251px}
  .c1{left:10px}.c2{left:312px}.c3{left:617px}.c4{left:926px}
  .slide-title{position:absolute;left:12px;top:5px;font-weight:700;font-size:12px;color:var(--title-blue);padding-bottom:2px;border-bottom:1px solid var(--title-blue)}
  .body{position:absolute;font-size:4.6px;line-height:6.2px;text-align:justify}
  .bullets{position:absolute;list-style:none;font-size:5px;font-weight:700;color:#333}
  .bullets li{line-height:9.6px;padding-left:9px;position:relative}
  .bullets li::before{content:"";position:absolute;left:0;top:2.6px;width:5px;height:5px;border-radius:50%;background:radial-gradient(circle at 35% 35%,#8fa3e0,var(--bullet))}
  .footer{position:absolute;left:0;right:0;bottom:0;height:17px;background:var(--footer);color:var(--white);font-family:"Arimo",sans-serif;font-weight:700;font-size:5.6px;letter-spacing:.3px;text-align:center;line-height:17px;border-top:2px solid #c7cde6}
  .media{position:absolute;border-radius:2px}
  .cover{background:radial-gradient(ellipse at 45% 30%,#3c52c8 0%,var(--navy) 50%,var(--navy-deep) 100%)}
  .cover .footer{background:linear-gradient(180deg,var(--lavender-light),var(--lavender));border-top:none;color:var(--white)}
  .brand{position:absolute;left:0;right:0;text-align:center;font-family:"Arimo",sans-serif;font-weight:700;color:var(--white)}
  .brand-name{font-size:20px;letter-spacing:1px;line-height:22px}
  .brand-sub{font-size:14px;line-height:16px}
  .pres-title{position:absolute;left:0;right:0;top:155px;text-align:center;font-family:"Arimo",sans-serif;font-weight:700;font-size:15px;color:var(--white)}
  .contact{position:absolute;left:0;right:0;top:132px;text-align:center;font-family:"Arimo",sans-serif;font-weight:700;font-size:7.6px;line-height:11px;color:var(--white)}
  .photo-box{position:absolute;left:15px;top:27px;width:82px;height:70px;background:var(--white);border:1px solid #cfd3e2;box-shadow:0 1px 3px rgba(0,0,0,.3);display:flex;align-items:center;justify-content:center;text-align:center;font-family:"Arimo",sans-serif;font-size:13px;line-height:15px;color:#222}
  .sub h4{font-size:5.6px;color:var(--title-blue);font-weight:700;line-height:7px}
  .sub p{font-size:4.6px;line-height:6.2px;text-align:justify}
  .sub{position:absolute;width:115px}
</style>
</head>
<body>
<main class="deck">

  <section class="slide cover r1 c1">
    <div class="brand" style="top:70px">
      <div class="brand-name">NORVELLE</div>
      <div class="brand-sub">Capital Management</div>
    </div>
    <div class="pres-title">Presentation Title</div>
    <div class="footer">www.norvellecapmgmt.com</div>
  </section>

  <section class="slide r1 c2">
    <h2 class="slide-title">Investment Strategy</h2>
    <p class="body" style="left:12px;top:28px;width:240px">Lorem ipsum d olor sit amet, consectetuer adipiscing elit, sed diam nonummy nibh euismod tincidunt ut laoreet dolore magna aliquam erat volutpat. Ut wisi enim ad minim veniam, quis nostrud exerci tation ullamcorper suscipit lobortis nisl ut aliquip ex ea commodo consequat. Duis autem vel eum iriure dolor in hendrerit in vulputate velit esse molestie consequat, vel illum dolore eu feugiat nulla facilisis.</p>
    <ul class="bullets" style="left:12px;top:69px">
      <li>Lorem ipsum Lorem Lorem ipsum Lorem Lorem ipsum</li>
      <li>Lorem ipsum Lorem Lorem Lorem Lorem ipsum</li>
      <li>Lorem ipsum Lorem Lorem ipsum Lorem Lorem ips</li>
    </ul>
    <div class="media" role="img" aria-label="Photo of a pen resting on a blue 3D pie chart and financial report" style="left:8px;top:98px;width:250px;height:80px;background:linear-gradient(120deg,#e6ebf5 0%,#9fbbe6 40%,#5b8fd6 60%,#dfe4ee 100%)"></div>
    <div class="footer">www.norvellecapmgmt.com</div>
  </section>

  <section class="slide r1 c3">
    <h2 class="slide-title">Financial Returns</h2>
    <p class="body" style="left:12px;top:28px;width:240px">Lorem ipsum d olor sit amet, consectetuer adipiscing elit, sed diam nonummy nibh euismod tincidunt ut laoreet dolore magna aliquam erat volutpat. Ut wisi enim ad minim veniam, quis nostrud exerci tation ullamcorper suscipit lobortis nisl ut aliquip ex ea commodo consequat. Duis autem vel eum iriure dolor in hendrerit in vulputate velit esse molestie consequat, vel illum dolore eu feugiat nulla facilisis.</p>
    <ul class="bullets" style="left:12px;top:71px">
      <li>Lorem ipsum Lorem Lorem ipsum Lorem Lorem ipsum</li>
      <li>Lorem ipsum Lorem Lorem Lorem Lorem ipsum</li>
      <li>Lorem ipsum Lorem Lorem ipsum Lorem Lorem ipsum</li>
      <li>Lorem ipsum Lorem Lorem</li>
      <li>Lorem ipsum Lorem Lorem ipsum</li>
      <li>Lorem ipsum orem Lorem Lo</li>
      <li>Lorem ipsum Lorem Lore</li>
    </ul>
    <div class="media" role="img" aria-label="Photo of a cheerful businessman in a blue shirt holding cash in both hands" style="left:135px;top:106px;width:122px;height:76px;background:linear-gradient(180deg,#eef1f7 0%,#7da6df 55%,#2f6cc2 100%)"></div>
    <div class="footer">www.norvellecapmgmt.com</div>
  </section>

  <section class="slide r1 c4">
    <h2 class="slide-title">Manager Biography</h2>
    <div class="photo-box">Your Photo Here</div>
    <p class="body" style="left:106px;top:28px;width:148px">Lorem ipsum d olor sit amet, consectetuer adipiscing elit, sed diam nonummy nibh euismod tincidunt ut laoreet dolore magna aliquam erat volutpat. Ut wisi enim ad minim veniam, quis nostrud exerci tation ullamcorper suscipit lobortis nisl ut aliquip ex ea commodo consequat. Duis autem vel eum iriure dolor in hendrerit in vulputate velit esse molestie consequat, vel illum dolore eu feugiat nulla facilisis.</p>
    <ul class="bullets" style="left:12px;top:101px">
      <li>Lorem ipsum Lorem Lorem ipsum Lorem Lorem ipsum</li>
      <li>Lorem ipsum Lorem Lorem Lorem Lorem ipsum</li>
      <li>Lorem ipsum Lorem Lorem ipsum Lorem Lorem ipsum</li>
    </ul>
    <p class="body" style="left:12px;top:133px;width:240px">Lorem ipsum d olor sit amet, consectetuer adipiscing elit, sed diam nonummy nibh euismod tincidunt ut laoreet dolore magna aliquam erat volutpat. Ut wisi enim ad minim veniam, quis nostrud exerci tation ullamcorper suscipit lobortis nisl ut aliquip ex ea commodo consequat. Duis autem vel eum iriure dolor in hendrerit in vulputate velit esse molestie conseq.</p>
    <div class="footer">www.norvellecapmgmt.com</div>
  </section>

  <section class="slide r2 c1">
    <h2 class="slide-title">Lorem Ipsum</h2>
    <p class="body" style="left:12px;top:28px;width:240px">Lorem ipsum d olor sit amet, consectetuer adipiscing elit, sed diam nonummy nibh euismod tincidunt ut laoreet dolore magna aliquam erat volutpat. Ut wisi enim ad minim veniam, quis nostrud exerci tation ullamcorper suscipit lobortis nisl ut aliquip ex ea commodo consequat. Duis autem vel eum iriure dolor in hendrerit in vulputate velit esse molestie consequat, vel illum dolore eu feugiat nulla facilisis.</p>
    <div class="media" role="img" aria-label="Illustration of a profit and loss gauge with a briefcase and stacked coins" style="left:12px;top:75px;width:120px;height:98px;background:radial-gradient(circle at 50% 60%,#fbf6c8 0%,#f0e3a0 45%,#d9dde8 75%,rgba(255,255,255,0) 100%)"></div>
    <p class="body" style="left:140px;top:78px;width:113px">Lorem ipsum d olor sit amet, consectetuer adipiscing elit, sed diam nonummy nibh euismod tincidunt ut laoreet dolore magna aliquam erat volutpat. Ut wisi enim ad minim veniam, quis nostrud exerci tation.</p>
    <p class="body" style="left:140px;top:127px;width:113px">Lorem ipsum d olor sit amet, consectetuer adipiscing elit, sed diam nonummy nibh euismod tincidunt ut laoreet dolore magna aliquam erat volutpat. Ut wisi enim ad minim veniam, quis nostrud exerci tation.</p>
    <div class="footer">www.norvellecapmgmt.com</div>
  </section>

  <section class="slide r2 c2">
    <h2 class="slide-title">Lorem Ipsum</h2>
    <p class="body" style="left:12px;top:28px;width:240px">Lorem ipsum d olor sit amet, consectetuer adipiscing elit, sed diam nonummy nibh euismod tincidunt ut laoreet dolore magna aliquam erat volutpat. Ut wisi enim ad minim veniam, quis nostrud exerci tation ullamcorper suscipit lobortis nisl ut aliquip ex ea commodo consequat. Duis autem vel eum iriure dolor in hendrerit in vulputate velit esse molestie consequat, vel illum dolore eu feugiat nulla facilisis.</p>
    <p class="body" style="left:12px;top:78px;width:115px">Lorem ipsum d olor sit amet, consectetuer adipiscing elit, sed diam nonummy nibh euismod tincidunt ut laoreet dolore magna aliquam erat volutpat. Ut wisi enim ad minim veniam, quis nostrud exerci tation.</p>
    <p class="body" style="left:12px;top:127px;width:115px">Lorem ipsum d olor sit amet, consectetuer adipiscing elit, sed diam nonummy nibh euismod tincidunt ut laoreet dolore magna aliquam erat volutpat. Ut wisi enim ad minim veniam, quis nostrud exerci tation.</p>
    <div class="media" role="img" aria-label="Photo of a large pile of dollar bills" style="left:132px;top:100px;width:128px;height:80px;background:radial-gradient(ellipse at 60% 55%,#a9b59a 0%,#7f8c70 45%,#e6e8e2 85%,rgba(255,255,255,0) 100%)"></div>
    <div class="footer">www.norvellecapmgmt.com</div>
  </section>

  <section class="slide r2 c3">
    <h2 class="slide-title">Lorem Ipsum</h2>
    <div class="sub" style="left:12px;top:33px"><h4>Sub Title-1</h4><p>Lorem ipsum dolor sit amet, etuer.Lorem ipsum dolor sit amet, etuer.Lorem ipsum dolor sit amet, etuer.Lorem ipsum dolor sit</p></div>
    <div class="sub" style="left:142px;top:33px"><h4>Sub Title-1</h4><p>Lorem ipsum dolor sit amet, etuer.Lorem ipsum dolor sit amet, etuer.Lorem ipsum dolor sit amet, etuer.Lorem ipsum dolor sit</p></div>
    <div class="sub" style="left:12px;top:79px"><h4>Sub Title-2</h4><p>Lorem ipsum dolor sit amet, etuer.Lorem ipsum dolor sit amet, etuer.Lorem ipsum dolor sit amet, etuer.Lorem ipsum dolor sit</p></div>
    <div class="sub" style="left:142px;top:79px"><h4>Sub Title-2</h4><p>Lorem ipsum dolor sit amet, etuer.Lorem ipsum dolor sit amet, etuer.Lorem ipsum dolor sit amet, etuer.Lorem ipsum dolor sit</p></div>
    <div class="sub" style="left:12px;top:125px"><h4>Sub Title-3</h4><p>Lorem ipsum dolor sit amet, etuer.Lorem ipsum dolor sit amet, etuer.Lorem ipsum dolor sit amet, etuer.Lorem ipsum dolor sit</p></div>
    <div class="sub" style="left:142px;top:125px"><h4>Sub Title-3</h4><p>Lorem ipsum dolor sit amet, etuer.Lorem ipsum dolor sit amet, etuer.Lorem ipsum dolor sit amet, etuer.Lorem ipsum dolor sit</p></div>
    <div class="footer">www.norvellecapmgmt.com</div>
  </section>

  <section class="slide cover r2 c4">
    <div class="brand" style="top:62px">
      <div class="brand-name">NORVELLE</div>
      <div class="brand-sub">Capital Management</div>
    </div>
    <address class="contact" style="font-style:normal">
      48 Harbor Ln. Newark, NJ 07102<br>
      Phone: 555-014-2280<br>
      Email: mreyes@norvellecapmgmt.com
    </address>
    <div class="footer">www.norvellecapmgmt.com</div>
  </section>

</main>
</body>
</html>
```